Brisket Electrical Business Card Design

A Registered Electrical Contractor with +21 years experience backed with advanced electrical and electronics education. The design should appeal to the industrial, commercial and domestic electrical industry. Final design should communicate prompt, diverse, professional service.
Updates

The Business Name is "Brisket Electrical" not brisket Electrical South Eastern Suburbs

Project Deadline Extended
Reason: I have committed payment, removed colour limitations and asked for images to be added so designers can have more freedom to capture the audience with the WOW factor. So go for it and show me what you got. GOOD LUCK EVERYONE

Target Market(s)

Target Industrial business sector, domestic faults and repairs.
We cover all electrical faults, power, lighting, installation, control wiring, machines, process lines, appliances, maintenance, compliance testing, overhead cranes, switchboards and more.

Industry/Entity Type

Electronics

Contact Information for Business Card

Brisket Electrical
South Eastern Suburbs
Melbourne, Victoria 3976
0497 315 248
brisketelectrical@mailhaven.example
ABN: 48 205 931 764
REC: 59037

Requirements
Must have
• 1 - "REC: 59037" should be at the top righthand corner.
2 - Trade picture to reflect wow factor. e.g Lighning, electrician.
3 - List format:( I will ask you to edit as required if design looks too cluttered)
Industrial, Commercial, Domestic, Manufacturing, Installation, Faults, Maintenance,
Commissioning, Compliance Testing, HV Equipment, Generators, Pumps, Overhead Cranes, Power, Lighting, Appliances, Leads, Process Lines, Control Wiring, Main Control Cubicles, Switchboards, Motor Control, VSD, PLC, Electronics, …
Nice to have
• The letters B and E as a combined shape to be used as a logo
Should not have
• "since 21 Year"

```html
<!DOCTYPE html>
<html lang="en">
<head>
<meta charset="utf-8">
<title>Brisket Electrical – Business Card</title>
<link rel="stylesheet" href="https://fonts.googleapis.com/css2?family=Source+Sans+3:wght@600;700&display=swap">
<style>
  :root {
    --canvas: #ffffff;
    --card-edge: #1a1a1a;
    --card-white: #ffffff;
    --lime: #9dcb3c;
    --signal-red: #ec1f27;
    --charcoal: #18181a;
    --slate: #58585a;
    --text-light: #ffffff;
  }
  * { box-sizing: border-box; margin: 0; padding: 0; }
  html, body {
    width: 1200px; height: 1200px; overflow: hidden;
    background: var(--canvas);
    font-family: "Source Sans 3", "Segoe UI", Arial, sans-serif;
  }
  .canvas {
    position: relative; width: 1200px; height: 1200px;
    border: 1px solid #6d6d6d;
  }
  .card {
    position: absolute; left: 68px; top: 266px;
    width: 1071px; height: 662px;
    background: var(--card-white);
    border: 2px solid var(--card-edge);
    overflow: hidden;
  }
  .brand {
    position: absolute; left: 86px; top: 60px;
    display: flex; align-items: center; gap: 44px;
  }
  .brand-mark {
    width: 150px; height: 150px;
    background: var(--signal-red);
  }
  .brand-name {
    font-weight: 700; font-size: 64px; line-height: 0.98;
    color: var(--slate); letter-spacing: 1px;
  }
  .lime-band {
    position: absolute; left: 0; right: 0; top: 290px; height: 280px;
    background: var(--lime);
  }
  .base-band {
    position: absolute; left: 0; right: 0; top: 570px; bottom: 0;
    background: var(--charcoal);
  }
  .rec-tab {
    position: absolute; left: 400px; top: 544px; right: 0; height: 58px;
    background: var(--signal-red);
    border: 3px solid var(--card-white); border-right: none;
    border-top-left-radius: 44px;
    display: flex; align-items: center; justify-content: flex-end;
    padding-right: 74px;
    color: var(--text-light); font-weight: 700; font-size: 34px;
  }
  .contact {
    position: absolute; right: 68px; top: 340px;
    color: var(--text-light); font-weight: 600; font-size: 31px;
    text-align: right;
  }
  .contact-line {
    display: flex; align-items: center; justify-content: flex-end;
    gap: 20px; height: 52px;
  }
  .contact-line svg { width: 40px; height: 34px; flex: none; }
  .contact-line.abn { margin-top: 14px; padding-right: 60px; }
</style>
</head>
<body>
<div class="canvas">
  <div class="card">
    <div class="brand">
      <div class="brand-mark"></div>
      <div class="brand-name">Brisket<br>Electrical</div>
    </div>

    <div class="lime-band"></div>
    <div class="base-band"></div>

    <div class="contact">
      <div class="contact-line phone">
        <span>0497 315 248</span>
        <svg viewBox="0 0 40 34" aria-hidden="true">
          <path d="M10 3 L16 9 L12 13 Q16 21 24 25 L28 21 L34 27 L28 32 Q14 30 6 14 Q6 7 10 3 Z" fill="#fff"/>
        </svg>
      </div>
      <div class="contact-line email">
        <span>brisketelectrical@mailhaven.example</span>
        <svg viewBox="0 0 40 34" aria-hidden="true">
          <rect x="3" y="7" width="34" height="22" fill="#fff"/>
          <path d="M3 7 L20 20 L37 7 M3 29 L15 17 M37 29 L25 17" stroke="#9dcb3c" stroke-width="2" fill="none"/>
        </svg>
      </div>
      <div class="contact-line abn">
        <span>ABN: 48 205 931 764</span>
      </div>
    </div>

    <div class="rec-tab">REC: 59037</div>
  </div>
</div>
</body>
</html>
```